Gym Membership Sales Sheet

I want this sheet to showcase the four contract types of bronze, silver, 6 month and platinum underneath of the three membership types of individual, partner and family. I am not particularly stuck on the bronze, silver, gold, platinum structure if you feel you have four better names that would work. However on the new sheet I want to remove the option for a 6 month contract. So, move up the PIF for just one year option and remove the three month option. Then remove everything else on the page. Add in hydromassage/tanning in with silver, gold and platinum contracts. The sheet needs to be simple.

Three membership types of individual, partner and family.

Then Bronze, silver, gold, platinum.

Silver, Gold and platinum members get hydromassage and tanning access. Only gold and platinum members get 15% of personal training and kinetics programs. Gold and Platinum members get free kid zone access as well.

Target Market(s)

Families, women and young adult males

Industry/Entity Type

Fitness

Colors
9bcb3c

Requirements
Must have
• Must have a cohesive design that highlights the membership types effectively. A design that is simple yet effective in causing people to choose Gold and Platinum plans. The goal of it is to up sell everyone into Gold and Platinum memberships.
Nice to have
• It would be nice to have three design types. One that appeals to women. One that appeals to young adult males and the third that appeals to families.
Should not have
• It should not be over complex and should not have a 6 month membership or 3 month membership options.

```html
<!DOCTYPE html>
<html lang="en">
<head>
<meta charset="utf-8">
<title>Rivo Fitness – Membership Plans</title>
<link href="https://fonts.googleapis.com/css2?family=Exo+2:wght@500;700;800&family=Roboto:wght@400;500&display=swap" rel="stylesheet">
<style>
  :root{
    --green:#9bcb3c;
    --green-soft:#a8cf94;
    --green-deep:#5fa33a;
    --ink:#1f1f1f;
    --cell:#2b2b2b;
    --cell-line:#444;
    --paper:#ffffff;
    --header-cell:#efefef;
    --star:#e7b53c;
    --stage:#e9e9e7;
  }
  *{box-sizing:border-box;margin:0;padding:0}
  html,body{width:1200px;height:1000px;overflow:hidden;background:var(--stage)}
  body{font-family:"Roboto",Arial,sans-serif;position:relative}

  .sheet{position:absolute;top:110px;width:520px;height:780px;overflow:hidden;box-shadow:0 6px 18px rgba(0,0,0,.18)}
  .sheet--plans{left:50px;background:var(--ink)}
  .sheet--cover{left:630px}

  /* plans sheet */
  .hero-photo{position:absolute;left:0;top:0;width:520px;height:300px;
    background:linear-gradient(160deg,#cfd3d6 0%,#9aa0a5 45%,#5b6066 100%)}
  .hero-brand{position:absolute;left:150px;top:70px;display:flex;align-items:center;gap:12px;
    font-family:"Exo 2",sans-serif;font-weight:800;font-size:46px;color:var(--ink);letter-spacing:2px}
  .hero-brand .dot{width:18px;height:18px;background:var(--green-deep)}
  .plans-title{position:absolute;left:0;right:0;top:200px;text-align:center;
    font-family:"Exo 2",sans-serif;font-weight:800;font-size:34px;color:#fff;letter-spacing:1px}
  .plans-title span{color:var(--green)}

  .plan-table{position:absolute;left:0;top:255px;width:520px;height:375px;background:var(--green-soft);
    display:grid;grid-template-columns:118px repeat(3,1fr);grid-template-rows:50px repeat(4,1fr);
    gap:6px;padding:8px 8px 8px 0}
  .col-head{background:var(--header-cell);border:2px solid var(--cell);display:flex;align-items:center;justify-content:center;
    font-family:"Exo 2",sans-serif;font-weight:500;font-size:18px;color:var(--ink);letter-spacing:1px;text-transform:uppercase}
  .row-head{background:var(--cell);color:#fff;display:flex;flex-direction:column;align-items:center;justify-content:center;
    font-family:"Exo 2",sans-serif;font-weight:800;font-size:18px;text-transform:uppercase}
  .stars{color:var(--star);font-size:14px;letter-spacing:2px}
  .price{background:var(--cell);border-bottom:6px solid var(--header-cell);color:#fff;
    display:flex;flex-direction:column;align-items:center;justify-content:center;
    font-family:"Exo 2",sans-serif;font-weight:700;font-size:22px;line-height:1.05}
  .term{display:flex;align-items:center;gap:4px}
  .term b{font-size:26px}
  .term small{font-size:9px;line-height:1;text-transform:uppercase;font-weight:500;text-align:left}
  .pay{font-size:9px;text-transform:uppercase;font-weight:500}
  .monthly{font-size:8px;font-weight:500}

  .plan-notes{position:absolute;left:0;right:0;top:645px;text-align:center;color:#fff;padding:0 30px}
  .plan-notes h3{font-family:"Exo 2",sans-serif;font-weight:800;font-size:17px;text-transform:uppercase;margin-bottom:4px}
  .plan-notes h3 .stars{font-size:16px}
  .plan-notes p{font-size:11px;line-height:1.45}
  .plan-notes .tanning{margin-top:18px;font-size:11px;text-transform:none}
  .plan-notes .tanning b{font-weight:500;text-transform:uppercase}

  /* cover sheet */
  .brick-wall{position:absolute;inset:0;background:linear-gradient(180deg,#3a3a3a 0%,#222 50%,#333 100%)}
  .cover-band{position:absolute;left:0;right:0;top:250px;height:200px;background:var(--paper);
    display:flex;align-items:center;justify-content:center;gap:18px;box-shadow:0 6px 14px rgba(0,0,0,.5)}
  .cover-band .dot{width:26px;height:26px;border-radius:50%;background:var(--green-deep)}
  .cover-band .name{font-family:"Exo 2",sans-serif;font-weight:800;font-size:58px;color:var(--ink);letter-spacing:3px}
</style>
</head>
<body>

<section class="sheet sheet--plans">
  <div class="hero-photo" role="img" aria-label="Photo of a trainer and a member working out in a gym"></div>
  <div class="hero-brand"><span class="dot"></span>RIVO FITNESS</div>
  <h2 class="plans-title">OUR MEMBERSHIP <span>PLANS</span></h2>

  <div class="plan-table">
    <div></div>
    <div class="col-head">Individual</div>
    <div class="col-head">Partner</div>
    <div class="col-head">Family</div>

    <div class="row-head"><span class="stars">★</span>Basic</div>
    <div class="price">$49.99</div>
    <div class="price">$69.99</div>
    <div class="price">$79.99</div>

    <div class="row-head"><span class="stars">★★</span>Standard</div>
    <div class="price"><span class="term"><b>12</b><small>Months<br>Contract</small></span>$69.99</div>
    <div class="price"><span class="term"><b>12</b><small>Months<br>Contract</small></span>$89.99</div>
    <div class="price"><span class="term"><b>12</b><small>Months<br>Contract</small></span>$99.99</div>

    <div class="row-head"><span class="stars">★★★</span>Premium</div>
    <div class="price"><span class="term"><b>18</b><small>Months<br>Contract</small></span>$59.99</div>
    <div class="price"><span class="term"><b>18</b><small>Months<br>Contract</small></span>$79.99</div>
    <div class="price"><span class="term"><b>18</b><small>Months<br>Contract</small></span>$89.99</div>

    <div class="row-head"><span class="stars">★★★★</span>Ultimate</div>
    <div class="price">1 YEAR<span class="pay">Full Payment</span>$480<span class="monthly">($40/month)</span></div>
    <div class="price">1 YEAR<span class="pay">Full Payment</span>$660<span class="monthly">($55/month)</span></div>
    <div class="price">1 YEAR<span class="pay">Full Payment</span>$840<span class="monthly">($70/month)</span></div>
  </div>

  <div class="plan-notes">
    <h3><span class="stars">★</span> Only Premium &amp; Ultimate <span class="stars">★</span></h3>
    <p>Members get 15% of personal training and kinetics programs.<br>Gold and Platinum members get free kid zone access as well.</p>
    <p class="tanning"><b>Standard, Premium &amp; Ultimate</b> members get hydromassage and tanning access.</p>
  </div>
</section>

<section class="sheet sheet--cover">
  <div class="brick-wall" role="img" aria-label="Dark painted brick wall background"></div>
  <div class="cover-band"><span class="dot"></span><span class="name">RIVO FITNESS</span></div>
</section>

</body>
</html>
```